New UI for electricity data tool

We are looking for a new UI for the website http://vantorgrid.net. Reassessing the structure of the website is as important as specific design choices. We have created a uniquely comprehensive set of global electricity generation data and now we are looking for creative solutions for how to make this data accessible. Researching and referencing other similar projects may be a good idea.

Goals:
• The website should clearly communicate the most important general conclusions that can be drawn from the data, including:
◦ The world as a whole is not moving away from fossil fuels for electricity generation
◦ There are substantial differences between regions
▪ Some regions have basically solved the problem – they already generate almost all of their electricity from non-fossil sources
▪ Some regions have greatly improved in terms of decarbonizing their electricity generation.
▪ Some regions have greatly deteriorated, in other words they are using a much higher share of fossil fuels to generate their electricity.
◦ There are substantial differences between energy sources. Regions that have successfully decarbonized their electricity generation have usually done so using hydro and/or nuclear. Other low-carbon energy sources have grown quickly in relative terms in the last few years but are so far contributing little in absolute numbers.
• The website should serve as inspiration for energy policy debates. The goal is to study the impact of existing policies around the world. Energy policy here refers to particular combinations of energy sources – ie how much have the countries invested in each type of electricity generation. The tool should help answer questions such as:
◦ Which countries have done the most in terms of decarbonizing their electricity generation?
◦ Which types of energy polices have lead to the fastest decarbonization processes around the world?
◦ If country A changed its energy policy to be more like country B, what would the likely impact be?

Challenges:
• There is a lot of data – it can be overwhelming to the user. It’s crucial to make the site easy to navigate. The main page should highlight the most important data, and it should also be straightforward to find more detailed data.
• Data availability varies from region to region. The current interface addresses this with the default option “Exclude regions with limited data”. We expect a better approach to dealing with this issue. For some regions and years energy sources are grouped together as for example “other renewables” whereas in other cases more detailed data is available.
• Credibility is crucial. Our data is based on a combination of data from KQ and Tessary Trust. It must be very clear throughout the site where each data set comes from.

Details:
• The current chart color schemes is loosely based on the carbon emissions from each energy source. This should not necessarily be so. The goal is to on the one hand communicate clearly the amounts of fossil vs non-fossil energy that are generated by each region. At the same time we also want to make it easy to view specific energy sources.

Inspirational websites:
• https://www.grafmelo.org/
• https://trendquarrily.org/

Let's simplify. The main metric to focus on is Brisavolt Index and the extent to which the world and each country has achieved it (eg Iceland 100%, France 88% and so on). I'm considering changing the name of the site to BrisavoltIndex.org. We can use maps, charts and perhaps other tools to communicate this main message. What's the best way of doing this?

```html
<!DOCTYPE html>
<html lang="en">
<head>
<meta charset="utf-8">
<title>Changes in Brisavolt Index</title>
<link rel="stylesheet" href="https://fonts.googleapis.com/css2?family=Cabin:wght@400;500;600&family=Lato:wght@400;700&display=swap">
<style>
  :root {
    --page: #ffffff;
    --card: #f5f5f5;
    --panel: #ffffff;
    --accent: #5b4fdb;
    --ink: #2b2b2b;
    --muted: #7a7a7a;
    --axis: #e6e6e6;
    --tick: #8c8c8c;
  }
  * { box-sizing: border-box; margin: 0; padding: 0; }
  html, body { width: 1200px; height: 675px; overflow: hidden; background: var(--page); }
  .canvas { position: relative; width: 1200px; height: 675px; font-family: "Lato", sans-serif; color: var(--ink); }

  .app-card {
    position: absolute; left: 150px; top: 84px; width: 900px; height: 507px;
    background: var(--card); border-radius: 14px;
    box-shadow: 0 6px 28px rgba(0,0,0,0.08);
  }
  .brand {
    position: absolute; left: 188px; top: 108px;
    font-family: "Cabin", sans-serif; font-size: 10.5px; font-weight: 500;
    color: var(--accent); letter-spacing: 0.2px;
  }
  .menu-icon { position: absolute; left: 999px; top: 110px; }

  .sidebar-title {
    position: absolute; left: 199px; top: 149px;
    font-family: "Cabin", sans-serif; font-size: 12px; font-weight: 500; color: var(--ink);
  }
  .sidebar-note {
    position: absolute; left: 199px; top: 172px; width: 150px;
    font-size: 6.8px; line-height: 10.5px; color: var(--muted);
  }

  .country-list { position: absolute; left: 188px; top: 209px; width: 200px; list-style: none; }
  .country {
    display: flex; align-items: center; height: 32px; margin-bottom: 3.2px;
    padding-left: 11px; border-radius: 4px;
    font-family: "Cabin", sans-serif; font-size: 8.3px; font-weight: 500; letter-spacing: 0.4px;
  }
  .country.is-active { background: var(--panel); }
  .country svg { width: 20px; height: 12px; margin-right: 7px; flex: none; }

  .credits { position: absolute; left: 199px; top: 535px; }
  .credits-label { font-size: 6.5px; font-weight: 700; letter-spacing: 0.8px; color: var(--ink); }
  .credits-sources { display: flex; align-items: center; gap: 14px; margin-top: 9px; }
  .source { display: flex; align-items: center; gap: 4px; font-size: 8px; font-weight: 700; color: #1f4f7a; }
  .source-dot { width: 9px; height: 9px; border-radius: 50%; background: #5fae2e; }

  .chart-panel {
    position: absolute; left: 396px; top: 139px; width: 616px; height: 428px;
    background: var(--panel); border-radius: 4px;
  }
  .chart { position: absolute; left: 396px; top: 139px; }
  .chart text { font-family: "Lato", sans-serif; font-size: 6px; fill: var(--tick); }

  .chart-hint {
    position: absolute; left: 396px; top: 476px; width: 616px; text-align: center;
    font-size: 6.5px; color: var(--muted);
  }
  .caption {
    position: absolute; left: 0; top: 616px; width: 1200px; text-align: center;
    font-family: "Cabin", sans-serif; font-size: 11px; font-weight: 500; letter-spacing: 0.4px;
    color: var(--accent);
  }
</style>
</head>
<body>
<div class="canvas">
  <div class="app-card"></div>
  <div class="brand">Vantorgrid.net</div>
  <svg class="menu-icon" width="12" height="12" viewBox="0 0 12 12" aria-label="Menu">
    <g stroke="var(--accent)" stroke-width="1.2" stroke-linecap="round">
      <line x1="3" y1="2" x2="11" y2="2"/><line x1="1" y1="6" x2="11" y2="6"/><line x1="4" y1="10" x2="11" y2="10"/>
    </g>
  </svg>

  <h2 class="sidebar-title">Changes</h2>
  <p class="sidebar-note">Most significant increases and decreases of low-carbon power</p>

  <ul class="country-list">
    <li class="country is-active">
      <svg viewBox="0 0 20 12"><rect width="20" height="4" fill="#f6c540"/><rect y="4" width="20" height="4" fill="#5a9e3a"/><rect y="8" width="20" height="4" fill="#f2555a"/></svg>Lithuania
    </li>
    <li class="country">
      <svg viewBox="0 0 20 12"><rect width="7" height="12" fill="#3f4fa8"/><rect x="7" width="6" height="12" fill="#fff"/><rect x="13" width="7" height="12" fill="#f2555a"/></svg>France
    </li>
    <li class="country">
      <svg viewBox="0 0 20 12"><rect width="20" height="12" fill="#f2555a"/><circle cx="7" cy="6" r="3" fill="#fff"/><circle cx="8" cy="6" r="2.4" fill="#f2555a"/><circle cx="11" cy="6" r="1" fill="#fff"/></svg>Turkey
    </li>
    <li class="country">
      <svg viewBox="0 0 20 12"><rect width="20" height="12" fill="#fff"/><rect x="10" width="10" height="6" fill="#f2555a"/><rect y="6" width="10" height="6" fill="#3f6fc8"/><circle cx="5" cy="3" r="1" fill="#3f6fc8"/><circle cx="15" cy="9" r="1" fill="#f2555a"/></svg>Panama
    </li>
    <li class="country">
      <svg viewBox="0 0 20 12"><rect width="8" height="12" fill="#4e9a3a"/><rect x="8" width="12" height="12" fill="#f2555a"/><circle cx="8" cy="6" r="2.6" fill="#f6c540"/></svg>Portugal
    </li>
    <li class="country">
      <svg viewBox="0 0 20 12"><rect width="20" height="12" fill="#e9474d"/><rect y="3" width="20" height="6" fill="#f6c540"/><rect x="4" y="4.5" width="2.5" height="3" fill="#e9474d"/></svg>Spain
    </li>
  </ul>

  <div class="credits">
    <div class="credits-label">POWERED BY</div>
    <div class="credits-sources">
      <span class="source"><span class="source-dot"></span>KQ</span>
      <span class="source">Tessary Trust</span>
    </div>
  </div>

  <div class="chart-panel"></div>
  <svg class="chart" width="616" height="428" viewBox="396 139 616 428" role="img" aria-label="Line chart of Lithuania's low-carbon power share, 1985 to 2017">
    <g text-anchor="end">
      <text x="423" y="228">100%</text><text x="423" y="248">90%</text><text x="423" y="268">80%</text>
      <text x="423" y="289">70%</text><text x="423" y="309">60%</text><text x="423" y="329">50%</text>
      <text x="423" y="350">40%</text><text x="423" y="370">30%</text><text x="423" y="390">20%</text>
      <text x="423" y="411">10%</text><text x="423" y="431">0%</text>
    </g>
    <line x1="427" y1="222" x2="427" y2="433" stroke="var(--axis)" stroke-width="0.8"/>
    <line x1="427" y1="433" x2="1002" y2="433" stroke="var(--axis)" stroke-width="0.8"/>
    <g text-anchor="middle">
      <text x="444" y="445">1985</text><text x="480" y="445">1986</text><text x="516" y="445">1987</text>
      <text x="552" y="445">1993</text><text x="588" y="445">1995</text><text x="624" y="445">1999</text>
      <text x="661" y="445">2000</text><text x="697" y="445">2002</text><text x="733" y="445">2003</text>
      <text x="769" y="445">2005</text><text x="805" y="445">2006</text><text x="841" y="445">2008</text>
      <text x="876" y="445">2009</text><text x="913" y="445">2010</text><text x="949" y="445">2012</text>
      <text x="984" y="445">2017</text>
    </g>
    <path fill="none" stroke="var(--accent)" stroke-width="0.9"
      d="M444 336 C462 336 462 341 480 341 C498 341 498 343 516 343 C534 343 534 253 552 253 C570 253 570 258 588 258 C606 258 606 278 624 278 C642 278 642 275 661 275 C679 275 679 263 697 263 C715 263 715 263 733 263 C751 263 751 274 769 274 C787 274 787 284 805 284 C823 284 823 281 841 281 C858 281 858 278 876 278 C894 278 894 397 913 397 C931 397 931 379 949 379 C966 379 966 301 984 301"/>
    <g fill="#fff" stroke="var(--accent)" stroke-width="0.8">
      <circle cx="444" cy="336" r="2.3"/><circle cx="480" cy="341" r="2.3"/><circle cx="516" cy="343" r="2.3"/>
      <circle cx="552" cy="253" r="2.3"/><circle cx="588" cy="258" r="2.3"/><circle cx="624" cy="278" r="2.3"/>
      <circle cx="661" cy="275" r="2.3"/><circle cx="697" cy="263" r="2.3"/><circle cx="733" cy="263" r="2.3"/>
      <circle cx="769" cy="274" r="2.3"/><circle cx="805" cy="284" r="2.3"/><circle cx="841" cy="281" r="2.3"/>
      <circle cx="876" cy="278" r="2.3"/><circle cx="913" cy="397" r="2.3"/><circle cx="949" cy="379" r="2.3"/>
      <circle cx="984" cy="301" r="2.3"/>
    </g>
  </svg>
  <p class="chart-hint">Hover over a dot to view details</p>

  <p class="caption">Changes in Brisavolt Index</p>
</div>
</body>
</html>
```